Medical Practice Business Card

we need a business card for our new medical ophthalmology practice based in Ashbury Massachusetts. we are looking for a simple , modern and elegant design.
the card needs to contain the following
1- the logo of our practice (please see attached file)
2- the name of the practice : "Silver Birch Eye Clinic"
3- Doctor's Name: Tobias Rendell MD PhD
4- Specialty: Board-Certified Vitreoretinal Surgeon
5- practice address: 87 Larkspur Ave, Suite 210, Ashbury MA 02481
7- Office number: 617- 482 - 7730
8- fax number: 617- 391 - 2268
9- email: info@sbretinahub.example
10- website: www.sbretinahub.example

```html
<!DOCTYPE html>
<html lang="en">
<head>
<meta charset="utf-8">
<title>Silver Birch Eye Clinic – Business Card</title>
<link href="https://fonts.googleapis.com/css2?family=Libre+Baskerville:wght@400;700&display=swap" rel="stylesheet">
<style>
  :root {
    --backdrop: #c4e8f9;
    --paper: #ffffff;
    --navy: #1a3a66;
    --royal: #1c5fb0;
    --ink: #1d2f55;
    --grad-start: #0257a0;
    --grad-end: #50b0d3;
    --mark: #2a2a2a;
  }
  * { margin: 0; padding: 0; box-sizing: border-box; }
  html, body { width: 1200px; height: 1200px; overflow: hidden; }
  body {
    background: var(--backdrop);
    position: relative;
    font-family: "Libre Baskerville", "Times New Roman", serif;
  }
  .card {
    position: absolute;
    left: 314px;
    width: 539px;
    height: 342px;
  }
  .card--front { top: 250px; background: var(--paper); }
  .card--back {
    top: 651px;
    background: linear-gradient(90deg, var(--grad-start) 0%, var(--grad-start) 7%, var(--grad-end) 100%);
  }
  .front-band {
    position: absolute;
    left: 0; right: 0; bottom: 0;
    height: 37px;
    background: linear-gradient(90deg, var(--grad-start) 0%, var(--grad-end) 100%);
  }
  .brand {
    position: absolute;
    font-weight: 400;
    line-height: 1.2;
    white-space: nowrap;
  }
  .card--front .brand {
    left: 70px; top: 142px;
    color: var(--navy);
    font-size: 22px;
  }
  .card--back .brand {
    left: 50%; top: 130px; transform: translateX(-50%);
    color: #ffffff;
    font-size: 32px;
  }
  .divider {
    position: absolute;
    left: 269px; top: 92px;
    width: 1px; height: 157px;
    background: var(--royal);
  }
  .person { position: absolute; left: 286px; top: 101px; }
  .person__name {
    font-size: 12.5px; font-weight: 700; color: var(--royal);
    letter-spacing: -0.2px;
  }
  .person__title {
    margin-top: 3px;
    font-size: 6.8px; color: var(--ink); letter-spacing: 0.1px;
  }
  .contacts {
    position: absolute; left: 286px; top: 152px;
    list-style: none; color: var(--ink); font-size: 9.8px;
  }
  .contacts li {
    display: flex; align-items: flex-start; gap: 6px;
    height: 17.7px; line-height: 14px;
  }
  .contacts li.address { height: auto; }
  .contacts svg { flex: none; width: 13px; height: 13px; }
  .address__line2 { display: block; margin-top: 4px; }
  .website {
    position: absolute; left: 0; right: 0; top: 280px;
    text-align: center; color: #ffffff;
    font-size: 13.5px; letter-spacing: 0.8px;
  }
  .crop-marks { position: absolute; left: 0; top: 0; }
</style>
</head>
<body>

<section class="card card--front">
  <p class="brand">Silver Birch<br>Eye Clinic</p>
  <div class="divider"></div>
  <div class="person">
    <p class="person__name">TOBIAS RENDELL MD PHD</p>
    <p class="person__title">BOARD-CERTIFIED VITREORETINAL SURGEON</p>
  </div>
  <ul class="contacts">
    <li>
      <svg viewBox="0 0 14 14" fill="none" stroke="#1c5fb0" stroke-width="0.8"><circle cx="7" cy="7" r="6.3"/><path d="M4.6 3.8 L5.8 3.6 L6.4 5.2 L5.7 5.9 Q6.6 7.7 8.2 8.4 L8.9 7.7 L10.4 8.3 L10.2 9.5 Q7.6 10.2 5.6 8.2 Q3.9 6.3 4.6 3.8Z"/></svg>
      <span>617- 482 - 7730</span>
    </li>
    <li>
      <svg viewBox="0 0 14 14" fill="none" stroke="#1c5fb0" stroke-width="0.8"><circle cx="7" cy="7" r="6.3"/><rect x="4" y="5.6" width="6" height="3.6" fill="#1c5fb0"/><rect x="5" y="3.6" width="4" height="2"/><rect x="5" y="8.6" width="4" height="1.8" fill="#fff"/></svg>
      <span>617- 391 - 2268</span>
    </li>
    <li>
      <svg viewBox="0 0 14 14" fill="none" stroke="#1c5fb0" stroke-width="0.8"><circle cx="7" cy="7" r="6.3"/><rect x="3.8" y="4.8" width="6.4" height="4.4"/><path d="M3.8 4.8 L7 7.3 L10.2 4.8"/></svg>
      <span>info@sbretinahub.example</span>
    </li>
    <li class="address">
      <svg viewBox="0 0 14 14" fill="none" stroke="#1c5fb0" stroke-width="0.8"><circle cx="7" cy="7" r="6.3"/><path d="M7 10.8 Q4.4 7.8 4.4 6 A2.6 2.6 0 0 1 9.6 6 Q9.6 7.8 7 10.8Z" fill="#1c5fb0"/><circle cx="7" cy="6" r="0.9" fill="#fff" stroke="none"/></svg>
      <span>87 larkspur ave, suite 210,<span class="address__line2">ashbury ma 02481</span></span>
    </li>
  </ul>
  <div class="front-band"></div>
</section>

<section class="card card--back">
  <p class="brand">Silver Birch<br>Eye Clinic</p>
  <p class="website">www.sbretinahub.example</p>
</section>

<svg class="crop-marks" width="1200" height="1200" viewBox="0 0 1200 1200" stroke="#2a2a2a" stroke-width="0.8" aria-hidden="true">
  <line x1="331" y1="231" x2="331" y2="260"/>
  <line x1="836" y1="231" x2="836" y2="260"/>
  <line x1="295" y1="267" x2="325" y2="267"/>
  <line x1="842" y1="267" x2="872" y2="267"/>
  <line x1="295" y1="576" x2="325" y2="576"/>
  <line x1="842" y1="576" x2="872" y2="576"/>
  <line x1="331" y1="582" x2="331" y2="611"/>
  <line x1="836" y1="582" x2="836" y2="611"/>
  <line x1="331" y1="632" x2="331" y2="661"/>
  <line x1="836" y1="632" x2="836" y2="661"/>
  <line x1="295" y1="668" x2="325" y2="668"/>
  <line x1="842" y1="668" x2="872" y2="668"/>
  <line x1="295" y1="976" x2="325" y2="976"/>
  <line x1="842" y1="976" x2="872" y2="976"/>
  <line x1="331" y1="982" x2="331" y2="1011"/>
  <line x1="836" y1="982" x2="836" y2="1011"/>
</svg>

</body>
</html>
```